Willowbend Pharmacy Business Cards

I need a business card design and or template. Needs to convey a softer feel along with health and wellness. Please see attached logo and color scheme.

Industry/Entity Type

Pharmacy

Colors

Designer to choose colors to be used in the design.

Requirements
Must have
• I've added a second NEW colored logo I think I am going to go with the blue green logo.
• Needs to have the colors and feel of the logo attached.
• Darrel Quimby
• Pharmacy Manager
• willowbendpharmacy.example

```html
<!DOCTYPE html>
<html lang="en">
<head>
<meta charset="utf-8">
<title>Willowbend Pharmacy – Business Cards</title>
<link rel="stylesheet" href="https://fonts.googleapis.com/css2?family=Roboto:wght@400;500;700&family=Roboto+Condensed:wght@700&display=swap">
<style>
  :root {
    --backdrop: #ecebe8;
    --card: #fbfbfa;
    --ink: #4a4a4d;
    --ink-soft: #5a5a5e;
    --brand-blue: #2f9bcd;
    --brand-green: #8cc63f;
    --rule: #b9b9bb;
  }
  * { margin: 0; padding: 0; box-sizing: border-box; }
  html, body {
    width: 1200px;
    height: 794px;
    overflow: hidden;
    background: var(--backdrop);
  }
  .card-set {
    position: relative;
    width: 1200px;
    height: 794px;
    display: flex;
    align-items: center;
    justify-content: center;
    gap: 40px;
  }
  .card {
    position: relative;
    width: 540px;
    height: 309px;
    background: var(--card);
    box-shadow: 0 2px 10px rgba(0,0,0,0.12);
    overflow: hidden;
    font-family: "Roboto", Arial, sans-serif;
  }

  /* Front */
  .card-front .brand {
    position: absolute;
    top: 112px;
    left: 0;
    width: 100%;
    display: flex;
    align-items: center;
    justify-content: center;
    gap: 14px;
  }
  .brand-dot {
    width: 44px;
    height: 44px;
    border-radius: 50%;
    background: var(--brand-green);
  }
  .brand-name {
    font-family: "Roboto", Arial, sans-serif;
    font-weight: 700;
    font-size: 30px;
    color: var(--ink);
    letter-spacing: -0.3px;
  }
  .card-front .website {
    position: absolute;
    bottom: 42px;
    left: 0;
    width: 100%;
    text-align: center;
    font-size: 12px;
    letter-spacing: 4px;
    color: var(--ink);
  }

  /* Back */
  .card-back .contact {
    position: absolute;
    left: 40px;
    top: 98px;
    width: 215px;
  }
  .person-name {
    font-family: "Roboto Condensed", "Arial Narrow", sans-serif;
    font-weight: 700;
    font-size: 17px;
    color: var(--brand-blue);
    line-height: 1;
  }
  .person-role {
    font-family: "Roboto Condensed", "Arial Narrow", sans-serif;
    font-weight: 700;
    font-size: 13px;
    color: var(--brand-green);
    margin-top: 3px;
  }
  .contact-line {
    font-size: 12.5px;
    color: var(--ink-soft);
    line-height: 1.35;
  }
  .divider {
    border: 0;
    border-top: 1px dotted var(--rule);
    margin: 5px 0 8px;
  }
  .contact .divider:first-of-type { margin-top: 6px; }
  .emblem-area {
    position: absolute;
    right: 38px;
    top: 50%;
    width: 200px;
    height: 200px;
    margin-top: -100px;
    border-radius: 50%;
    background: var(--brand-green);
  }
</style>
</head>
<body>
  <main class="card-set">
    <section class="card card-front" aria-label="Business card front">
      <div class="brand">
        <span class="brand-dot" aria-hidden="true"></span>
        <span class="brand-name">Willowbend Pharmacy</span>
      </div>
      <p class="website">www.willowbendpharmacy.example</p>
    </section>

    <section class="card card-back" aria-label="Business card back">
      <div class="contact">
        <p class="person-name">DARREL QUIMBY</p>
        <p class="person-role">PHARMACY MANAGER</p>
        <hr class="divider">
        <p class="contact-line">555 014 2290</p>
        <hr class="divider">
        <p class="contact-line">555 017 3381</p>
        <p class="contact-line">darrel@willowbendpharmacy.example</p>
      </div>
      <div class="emblem-area" aria-hidden="true"></div>
    </section>
  </main>
</body>
</html>
```